Sticker label design for - Tidal Fern Deodorant Balm

I need a label for my 100% Natural Deodorant Balm
The brand is called "Plum Meadow Brand", and the product is called TIDAL FERN Deodorant Balm.
There are two labels, one is a 5.2cm circle for the top, and 4.5cm circle for the base. The jar is amber plastic with black lid.
Width: 5.8cm
Height: 3.4cm (Lid 1.2cm, base 2,2cm)
Here is a link to what the jar looks like from one of my competitors: https://copperwren.com.au/products/body/velaro-deodorant-paste/
The product is a unisex product. Please see uploaded files for designs previously made for the brand. I'm trying to see a few more designs before finalising my choice. Feel free to use the logo at the top (Plum Meadow Brand) of either attachment if you would like. Or design your own.
Be be aware that it is meant to be Aluminium and Paraben Free, not "Parabens" Weight of product is 70g, please include this.
Label can be any colour, and printed with regular colours or event gold, silver or rose gold foil. Would a background be nice?
This is something I saw that I liked:
http://www.mossvelbalm.com
However I'm really open to what people can come up with.
For the back base-
Tidal Fern deodorant balm is made from 100% natural ingredients, and works by neutralises odour and minimising wetness without the use of harmful chemicals.
www.plummeadowbrand.com
Directions: For optimal result, apply a pea size amount of the balm to your dry armpits. Gently rub the balm into your armpits covering the entire area. Discontinue use if irritation occurs.
Ingredients: Shea Butter, Coconut oil, Sodium Bicarbonate, Arrowroot, Kaolin Clay, Vitamin E, Vegetable Glycerin, Activated Charcoal, Essential oils of Peppermint, Lavender, Mandarin, Tea tree, Geranium Rose & Cedarwood.
MADE IN AUSTRALIA
Reason: Hi,
I'm not getting many submissions, so was hoping to extend the deadline.
Skin Care Product

```html
<!DOCTYPE html>
<html lang="en">
<head>
<meta charset="utf-8">
<title>Tidal Fern Deodorant Balm – Label Set</title>
<link rel="stylesheet" href="https://fonts.googleapis.com/css2?family=Kalam:wght@700&family=Montserrat:wght@600;700&family=Raleway:wght@400&display=swap">
<style>
  :root {
    --backdrop: #595959;
    --label-black: #1c1c1c;
    --gold-foil: #e4d092;
    --rose-foil: #d98f86;
  }
  html, body {
    margin: 0;
    width: 1200px;
    height: 802px;
    overflow: hidden;
    background: var(--backdrop);
  }
  .label-sheet {
    width: 1200px;
    height: 802px;
    display: grid;
    grid-template-columns: 1fr 1fr;
    grid-template-rows: 430px 372px;
    place-items: center;
  }
  .label { display: block; }
  .label--gold { --foil: var(--gold-foil); }
  .label--rose { --foil: var(--rose-foil); }
  .label-base { fill: var(--label-black); }
  .foil-line { fill: none; stroke: var(--foil); }
  .foil-text { fill: var(--foil); }
  .flourish-area { fill: var(--foil); opacity: 0.35; }
  .brand-name { font-family: "Montserrat", sans-serif; font-weight: 600; }
  .product-name { font-family: "Kalam", cursive; font-weight: 700; }
  .product-type { font-family: "Raleway", sans-serif; font-weight: 400; }
  .claims { font-family: "Montserrat", sans-serif; font-weight: 700; }
  .natural-claim { font-family: "Montserrat", sans-serif; font-weight: 700; letter-spacing: 1px; }
</style>
</head>
<body>
<main class="label-sheet">

  <!-- Gold lid label -->
  <svg class="label label--gold lid-label" width="370" height="370" viewBox="0 0 320 320">
    <circle class="label-base" cx="160" cy="160" r="156"/>
    <circle class="foil-line" cx="160" cy="160" r="143" stroke-width="10"/>
    <circle class="foil-line" cx="160" cy="160" r="131" stroke-width="1.5"/>
    <text class="foil-text brand-name" x="160" y="72" font-size="12" text-anchor="middle">PLUM MEADOW</text>
    <text class="foil-text brand-name" x="160" y="82" font-size="6.5" letter-spacing="3" text-anchor="middle">BRAND</text>
    <rect class="flourish-area" x="128" y="89" width="64" height="22" rx="11" role="img" aria-label="Decorative foil flourish beneath the brand name"/>
    <text class="foil-text product-name" x="160" y="153" font-size="42" text-anchor="middle">Tidal Fern</text>
    <text class="foil-text product-type" x="160" y="171" font-size="13" text-anchor="middle">Deodorant Balm</text>
    <text class="foil-text claims" x="160" y="198" font-size="7.5" text-anchor="middle">ALUMINIUM &amp; PARABEN FREE</text>
    <text class="foil-text claims" x="160" y="208" font-size="7.5" text-anchor="middle">VEGAN</text>
    <text class="foil-text claims" x="160" y="218" font-size="7.5" text-anchor="middle">CRUELTY FREE</text>
    <path id="arc-gold" d="M96 250 Q160 250 230 226" fill="none"/>
    <text class="foil-text natural-claim" font-size="15"><textPath href="#arc-gold">%100NATURAL</textPath></text>
  </svg>

  <!-- Rose lid label -->
  <svg class="label label--rose lid-label" width="370" height="370" viewBox="0 0 320 320">
    <circle class="label-base" cx="160" cy="160" r="156"/>
    <circle class="foil-line" cx="160" cy="160" r="143" stroke-width="10"/>
    <circle class="foil-line" cx="160" cy="160" r="131" stroke-width="1.5"/>
    <text class="foil-text brand-name" x="160" y="72" font-size="12" text-anchor="middle">PLUM MEADOW</text>
    <text class="foil-text brand-name" x="160" y="82" font-size="6.5" letter-spacing="3" text-anchor="middle">BRAND</text>
    <rect class="flourish-area" x="128" y="89" width="64" height="22" rx="11" role="img" aria-label="Decorative foil flourish beneath the brand name"/>
    <text class="foil-text product-name" x="160" y="153" font-size="42" text-anchor="middle">Tidal Fern</text>
    <text class="foil-text product-type" x="160" y="171" font-size="13" text-anchor="middle">Deodorant Balm</text>
    <text class="foil-text claims" x="160" y="198" font-size="7.5" text-anchor="middle">ALUMINIUM &amp; PARABEN FREE</text>
    <text class="foil-text claims" x="160" y="208" font-size="7.5" text-anchor="middle">VEGAN</text>
    <text class="foil-text claims" x="160" y="218" font-size="7.5" text-anchor="middle">CRUELTY FREE</text>
    <path id="arc-rose" d="M96 250 Q160 250 230 226" fill="none"/>
    <text class="foil-text natural-claim" font-size="15"><textPath href="#arc-rose">%100NATURAL</textPath></text>
  </svg>

  <!-- Gold base label -->
  <svg class="label label--gold base-label" width="340" height="220" viewBox="0 0 340 220">
    <path class="label-base" d="M40 20 H300 Q300 40 320 40 V180 Q300 180 300 200 H40 Q40 180 20 180 V40 Q40 40 40 20 Z"/>
    <path class="foil-line" stroke-width="3" d="M46 28 H294 Q296 46 312 48 V172 Q296 174 294 192 H46 Q44 174 28 172 V48 Q44 46 46 28 Z"/>
    <path class="foil-line" stroke-width="1" d="M52 35 H288 Q290 52 305 55 V165 Q290 168 288 185 H52 Q50 168 35 165 V55 Q50 52 52 35 Z"/>
    <text class="foil-text brand-name" x="170" y="56" font-size="9" text-anchor="middle">PLUM MEADOW</text>
    <text class="foil-text brand-name" x="170" y="64" font-size="5" letter-spacing="2.5" text-anchor="middle">BRAND</text>
    <rect class="flourish-area" x="152" y="68" width="36" height="10" rx="5" role="img" aria-label="Small decorative foil flourish"/>
    <text class="foil-text product-name" x="170" y="108" font-size="30" text-anchor="middle">Tidal Fern</text>
    <text class="foil-text product-type" x="170" y="122" font-size="10" text-anchor="middle">Deodorant Balm</text>
    <text class="foil-text claims" x="170" y="139" font-size="5.5" text-anchor="middle">ALUMINIUM &amp; PARABEN FREE</text>
    <text class="foil-text claims" x="170" y="147" font-size="5.5" text-anchor="middle">VEGAN</text>
    <text class="foil-text claims" x="170" y="155" font-size="5.5" text-anchor="middle">CRUELTY FREE</text>
    <text class="foil-text natural-claim" x="170" y="171" font-size="8.5" text-anchor="middle">%100 NATURAL</text>
  </svg>

  <!-- Rose base label -->
  <svg class="label label--rose base-label" width="340" height="220" viewBox="0 0 340 220">
    <path class="label-base" d="M40 20 H300 Q300 40 320 40 V180 Q300 180 300 200 H40 Q40 180 20 180 V40 Q40 40 40 20 Z"/>
    <path class="foil-line" stroke-width="3" d="M46 28 H294 Q296 46 312 48 V172 Q296 174 294 192 H46 Q44 174 28 172 V48 Q44 46 46 28 Z"/>
    <path class="foil-line" stroke-width="1" d="M52 35 H288 Q290 52 305 55 V165 Q290 168 288 185 H52 Q50 168 35 165 V55 Q50 52 52 35 Z"/>
    <text class="foil-text brand-name" x="170" y="56" font-size="9" text-anchor="middle">PLUM MEADOW</text>
    <text class="foil-text brand-name" x="170" y="64" font-size="5" letter-spacing="2.5" text-anchor="middle">BRAND</text>
    <rect class="flourish-area" x="152" y="68" width="36" height="10" rx="5" role="img" aria-label="Small decorative foil flourish"/>
    <text class="foil-text product-name" x="170" y="108" font-size="30" text-anchor="middle">Tidal Fern</text>
    <text class="foil-text product-type" x="170" y="122" font-size="10" text-anchor="middle">Deodorant Balm</text>
    <text class="foil-text claims" x="170" y="139" font-size="5.5" text-anchor="middle">ALUMINIUM &amp; PARABEN FREE</text>
    <text class="foil-text claims" x="170" y="147" font-size="5.5" text-anchor="middle">VEGAN</text>
    <text class="foil-text claims" x="170" y="155" font-size="5.5" text-anchor="middle">CRUELTY FREE</text>
    <text class="foil-text natural-claim" x="170" y="171" font-size="8.5" text-anchor="middle">%100 NATURAL</text>
  </svg>

</main>
</body>
</html>
```